Business card design needed

We require business cards for our young and innovative construction team.

Our business is Birch Constructions and we have used Lime, Navy and white with our colours so far.

We would like business cards that show our passion for perfection and detail, communication and management.

Looking forward to seeing the deigns!!

Industry/Entity Type

Communication

Contact Information for Business Card

Dan Prewitt
Birch Constructions Pty Ltd
PO Box 712 Carrow Ridge NSW 2177
Mobile: 0471 263 908
Email: dprewitt@birchconstructions.com.au
Web: www.birchconstructions.com.au

```html
<!DOCTYPE html>
<html lang="en">
<head>
<meta charset="utf-8">
<title>Birch Constructions – Business Card</title>
<link rel="stylesheet" href="https://fonts.googleapis.com/css2?family=Exo+2:wght@400;500&display=swap">
<style>
  :root {
    --lime: #9bcb34;
    --lime-deep: #7fae22;
    --navy: #3e4f86;
    --white: #ffffff;
    --paper: #f4f4f4;
    --backdrop: #e6e7e9;
    --card-w: 560px;
    --card-h: 342px;
  }
  * { box-sizing: border-box; margin: 0; padding: 0; }
  html, body {
    width: 1200px;
    height: 900px;
    overflow: hidden;
    background: var(--backdrop);
    font-family: "Exo 2", sans-serif;
  }
  .canvas {
    width: 1200px;
    height: 900px;
    display: flex;
    flex-direction: column;
    align-items: center;
    justify-content: center;
    gap: 60px;
  }
  .card {
    position: relative;
    width: var(--card-w);
    height: var(--card-h);
    overflow: hidden;
    box-shadow: 0 6px 18px rgba(0, 0, 0, 0.18);
  }

  /* Front side */
  .card--front {
    background: linear-gradient(135deg, #a3d13c 0%, var(--lime) 60%, #93c22e 100%);
  }
  .brand {
    position: absolute;
    display: flex;
    align-items: center;
    gap: 14px;
    color: var(--navy);
    font-weight: 500;
    white-space: nowrap;
  }
  .brand__mark {
    width: 26px;
    height: 26px;
    background: var(--white);
  }
  .card--front .brand {
    left: 50%;
    top: 128px;
    transform: translateX(-50%);
    font-size: 38px;
    letter-spacing: 1px;
  }
  .tagline {
    position: absolute;
    left: 0;
    right: 0;
    bottom: 48px;
    text-align: center;
    color: var(--white);
    font-size: 15px;
    letter-spacing: 0.5px;
  }

  /* Back side */
  .card--back {
    background: linear-gradient(160deg, var(--white) 0%, var(--paper) 100%);
  }
  .card--back .brand {
    right: 40px;
    top: 42px;
    font-size: 28px;
  }
  .card--back .brand__mark {
    width: 20px;
    height: 20px;
    background: var(--lime);
  }
  .person {
    position: absolute;
    left: 40px;
    top: 140px;
  }
  .person__name {
    color: var(--lime);
    font-size: 26px;
    font-weight: 500;
    line-height: 1.1;
  }
  .person__role {
    color: var(--navy);
    font-size: 18px;
    margin-top: 2px;
  }
  .contacts {
    margin-top: 18px;
    display: grid;
    grid-template-columns: 54px auto;
    row-gap: 4px;
    font-size: 15px;
  }
  .contacts dt { color: var(--lime); }
  .contacts dd { color: var(--navy); }
  .company {
    position: absolute;
    left: 360px;
    top: 140px;
    padding-left: 16px;
    border-left: 1px solid var(--lime);
    height: 82px;
    font-size: 14px;
    line-height: 1.45;
  }
  .company__name { color: var(--lime); font-weight: 500; }
  .company__address { color: var(--navy); font-style: normal; }
  .band {
    position: absolute;
    left: 0;
    right: 0;
    bottom: 0;
    height: 42px;
    background: linear-gradient(90deg, var(--lime) 0%, var(--lime-deep) 100%);
  }
</style>
</head>
<body>
<main class="canvas">

  <section class="card card--front" aria-label="Card front">
    <div class="brand"><span class="brand__mark"></span><span>Birch Constructions</span></div>
    <p class="tagline">Birch Constructions is a residential construction company</p>
  </section>

  <section class="card card--back" aria-label="Card back">
    <div class="brand"><span class="brand__mark"></span><span>Birch Constructions</span></div>

    <div class="person">
      <h1 class="person__name">Dan Prewitt</h1>
      <p class="person__role">Founder and Owner</p>
      <dl class="contacts">
        <dt>Mob</dt><dd>0471 263 908</dd>
        <dt>Email</dt><dd>dprewitt@birchconstructions.com.au</dd>
        <dt>Web</dt><dd>www.birchconstructions.com.au</dd>
      </dl>
    </div>

    <div class="company">
      <p class="company__name">Birch Constructions Pty Ltd</p>
      <address class="company__address">PO Box 712 Carrow Ridge<br>NSW 2177</address>
    </div>

    <div class="band"></div>
  </section>

</main>
</body>
</html>
```